Storm Restoration Contractor needs a professional letterhead design

Looking for a professional letterhead design. Not looking for your cheapo MS Word standard ones that are readily available. Dont want it to be cookie cutter look like ones readily available online. We just recently changed our logo and want to freshen up all our documents. Our company handles restoring a property back to a pre-loss condition after a storm damages it. For example, wind, hail, flood, fire losses.

Target Market(s)

Property Owners, Homeowners, Property Owners, Commercial Property Owners, Property Management Companies

Industry/Entity Type

Construction Company

Requirements
Must have
• Professional, Use 1 of 2 logo options
• Storm Restoration, Roofing, Siding, Windows

```html
<!DOCTYPE html>
<html lang="en">
<head>
<meta charset="utf-8">
<title>Stoneridge Exteriors — Letterhead and Folder</title>
<link href="https://fonts.googleapis.com/css2?family=Didact+Gothic&family=Lato:wght@400;700&display=swap" rel="stylesheet">
<style>
  :root {
    --backdrop: #e6eaec;
    --paper: #ffffff;
    --folder: #dcdcdc;
    --folder-light: #e4e4e4;
    --brand-blue: #1a7bc4;
    --ink: #333333;
    --rule: #6b6b6b;
    --muted: #555555;
  }
  * { box-sizing: border-box; margin: 0; padding: 0; }
  html, body { width: 1200px; height: 784px; overflow: hidden; }
  body { background: var(--backdrop); position: relative; font-family: "Didact Gothic", sans-serif; }

  .letterhead {
    position: absolute; left: 42px; top: 45px; width: 513px; height: 697px;
    background: var(--paper); border-radius: 12px; overflow: hidden;
  }
  .brand {
    position: absolute; display: flex; align-items: center; gap: 8px;
    font-family: "Lato", sans-serif; font-weight: 700; color: var(--brand-blue);
    text-transform: uppercase; line-height: 1;
  }
  .brand .mark { border-radius: 50%; background: var(--brand-blue); flex: none; }
  .letterhead .brand { left: 48px; top: 44px; font-size: 13.5px; letter-spacing: 0.5px; }
  .letterhead .brand .mark { width: 34px; height: 34px; }

  .contact {
    position: absolute; right: 40px; top: 47px; text-align: right;
    font-family: "Lato", sans-serif; font-size: 6.5px; color: var(--muted); line-height: 12.5px;
  }
  .contact .row { display: flex; justify-content: flex-end; align-items: center; gap: 5px; }
  .contact svg { width: 8px; height: 8px; fill: var(--brand-blue); }
  .contact .address { color: var(--brand-blue); font-weight: 700; }

  .header-rule { position: absolute; left: 48px; top: 110px; width: 425px; height: 2px; background: var(--rule); }

  .watermark {
    position: absolute; left: 190px; top: 258px; width: 150px; height: 150px;
    border-radius: 50%; background: var(--brand-blue); opacity: 0.07;
  }

  .body-copy {
    position: absolute; left: 48px; top: 143px; width: 425px;
    font-size: 10.6px; line-height: 17.6px; color: var(--ink); text-align: justify;
    hyphens: auto;
  }
  .body-copy p + p { margin-top: 17.6px; }

  .signature { position: absolute; left: 384px; top: 584px; color: var(--ink); }
  .signature .name { font-size: 14px; }
  .signature .title { font-size: 9.5px; margin-top: 8px; }

  .footer-band {
    position: absolute; left: 0; bottom: 0; width: 100%; height: 29px;
    background: var(--brand-blue); color: #ffffff; text-align: center;
    font-family: "Lato", sans-serif; font-size: 7px; letter-spacing: 1.6px; line-height: 29px;
  }

  .folder {
    position: absolute; left: 634px; top: 45px; width: 513px; height: 697px;
    background: linear-gradient(160deg, var(--folder-light), var(--folder)); border-radius: 12px;
  }
  .folder .brand { left: 128px; top: 566px; font-size: 27px; gap: 16px; letter-spacing: 1px; }
  .folder .brand .mark { width: 66px; height: 66px; }
</style>
</head>
<body>
  <section class="letterhead">
    <div class="brand"><span class="mark"></span>Stoneridge<br>Exteriors</div>

    <div class="contact">
      <div class="row">(555) 203-8896
        <svg viewBox="0 0 10 10"><path d="M2 1l2 2-1 1.2c.6 1.2 1.5 2.1 2.8 2.8L7 6l2 2-1.3 1.3C4.5 9 1 5.5.7 2.3z"/></svg></div>
      <div class="row">(555) 318-2640
        <svg viewBox="0 0 10 10"><rect x="2.5" y="0.5" width="5" height="3"/><rect x="0.5" y="3.5" width="9" height="4" rx="1"/><rect x="2.5" y="6.5" width="5" height="3"/></svg></div>
      <div class="row">info@stoneridgeexteriors.example
        <svg viewBox="0 0 10 10"><path d="M0.5 2h9v6h-9z M0.5 2l4.5 3.5L9.5 2" stroke="#fff" stroke-width=".6"/></svg></div>
      <div class="row address">480 Harbor Mill Road, 2nd Floor, Dalton, GA 30720</div>
    </div>

    <div class="header-rule"></div>
    <div class="watermark" aria-hidden="true"></div>

    <div class="body-copy">
      <p>Lorem ipsum dolor sit amet, consectetur adipiscing elit. Donec orci purus, luctus vitae dignissim eu, iaculis sed purus. Vivamus faucibus, ipsum nec aliquet viverra, leo mauris condimentum ligula, sit amet sagittis enim ligula quis arcu. Nam egestas tortor id nisi porttitor mattis. In tortor ante, ultricies in suscipit a, tempus non massa. Vivamus et auctor mi. Fusce vel massa nulla. Phasellus nec eros mauris, et scelerisque orci. Donec malesuada orci vitae nulla accumsan porta a id massa.</p>
      <p>Quisque accumsan iaculis magna sit amet fringilla. Maecenas consequat, magna eget tincidunt semper, odio nibh rutrum mi, id feugiat ante nisi eu risus. Vestibulum nunc orci, rhoncus a placerat in, ultricies in mi. Cras mattis varius eros, vel fringilla nisi suscipit eget. Quisque scelerisque sagittis nulla at porttitor. Mauris a justo et tellus interdum tristique. Sed id augue vitae urna euismod commodo aliquet a quam. Pellentesque arcu velit, cursus et malesuada ut, consequat et diam. Nullam erat sem, rhoncus id ullamcorper vitae, rhoncus et arcu. In ultricies ultricies nulla.</p>
      <p>Kut rutrum nisi iaculis at. Donec eu magna a metus ornare faucibus. Fusce aliquet faucibus ultricies. Morbi semper, est id tincidunt gravida, sem arcu adipiscing lacus, ac bibendum nulla leo eu purus. Quisque nec diam sed risus consectetur a ccumsan quis quis nibh. Vestibulum id purus lorem. Donec eu magna a metus ornare faucibus. Fusce aliquet faucibus ultricies. Morbi semper, est id tincidunt gravida, sem arcu adipiscing lacus, ac bibendum nulla leo eu purus. Quisque nec diam sed risus consectetur a ccumsan quis quis nibh. Vestibulum id purus lorem.</p>
    </div>

    <div class="signature">
      <div class="name">Dana Whitfield</div>
      <div class="title">Co-Founder &amp; CEO</div>
    </div>

    <div class="footer-band">www.stoneridgeexteriors.example</div>
  </section>

  <section class="folder">
    <div class="brand"><span class="mark"></span>Stoneridge<br>Exteriors</div>
  </section>
</body>
</html>
```